Premium small-production winery needs a front label redesign

We produce wine from cold-climate varietal grapes, many of which were only developed in the last 50 years. Our winery, called Harrow Ridge Cellars, is housed in an industrial style building serving a premium product. We have 12 styles of wine that can accommodate a wide range of tastes. We would like to see designs that communicate old traditions (winemaking styles) blended with new ideas (newly developed grape varieties). Our ideal customer enjoys an evening that is cultured and classy, yet fun and educational. We will likely favor designs that are 4" x 4.5", but this isn't required - if we see something we love, we would consider changing the dimensions.
I've attached our current labels and 2 logo files. We are only looking for a front-label redesign. Thanks!

Target Market(s)

Our ideal customer enjoys an evening that is cultured and classy, yet fun and educational.

Font styles to use
Serif
Sans Serif
Script
Other font styles liked:
• Our current fonts are Trajan Pro, Tangerine, and Avenir.

Requirements
Must have
• We would love to see a design that could span our entire product line with only a subtle or minor change (such as printing color, or a picture) to distinguish between our 12 products. Emphasis on the part about the change should be subtle among labels.
• Some of the distinguishing characteristics of the wines:
• Color: white, orange, rosé (pink), light red, dark red
• Sweetness: dry, off-dry, semi-sweet, sweet, very sweet
• Flavors: too many to list
• Product names: 9 of the wines are named after the majority grape. The other 3 are blends of multiple grapes, with the following names: "Velmora Blush", "Opal", and "Thistle".
Nice to have
• our wine list: http://harrowridgecellars.example/wine/
Should not have
• We would prefer a design that isn't too busy overall.

```html
<!DOCTYPE html>
<html lang="en">
<head>
<meta charset="utf-8">
<title>Harrow Ridge Cellars – Front Label Series</title>
<link rel="stylesheet" href="https://fonts.googleapis.com/css2?family=Cinzel:wght@400&family=Italianno&display=swap">
<style>
  :root {
    --board-dark: #26401b;
    --board-mid: #3f6131;
    --board-light: #50793f;
    --label-black: #000000;
    --label-pearl: #e6e6e6;
    --label-rose: #ffdaf8;
    --label-cream: #f8fdc8;
    --ink-dark: #111111;
    --ink-plum: #1f0b1e;
    --ink-light: #eef2e6;
    --ink-sage: #6e807c;
    --wine-red: #c51f2b;
    --wine-violet: #8c1e88;
    --wine-amber: #b8651c;
  }
  * { margin: 0; padding: 0; box-sizing: border-box; }
  html, body { width: 1200px; height: 1091px; overflow: hidden; }
  body {
    position: relative;
    background: linear-gradient(90deg,
      var(--board-mid) 0%, var(--board-light) 26%, var(--board-mid) 45%,
      var(--board-light) 72%, var(--board-dark) 100%);
    border: 1px solid #1d3214;
  }
  .label {
    position: absolute;
    width: 401px;
    height: 449px;
  }
  .label-shape { position: absolute; inset: 0; width: 401px; height: 449px; }
  .label--geneva { left: 169px; top: 74px; }
  .label--velmora { left: 640px; top: 74px; }
  .label--frontenac { left: 169px; top: 578px; }
  .label--crescent { left: 640px; top: 578px; }

  .label-text {
    position: absolute;
    right: 42px;
    text-align: right;
    white-space: nowrap;
  }
  .brand-mark {
    top: 160px;
    font-family: "Cinzel", serif;
    font-size: 22px;
    letter-spacing: 1px;
  }
  .brand-name {
    top: 252px;
    font-family: "Cinzel", serif;
    font-size: 26px;
    line-height: 31px;
  }
  .brand-name .line-sub { display: block; }
  .wine-name {
    top: 338px;
    font-family: "Italianno", cursive;
    font-size: 40px;
    line-height: 44px;
  }
  .wine-origin {
    top: 380px;
    font-family: "Italianno", cursive;
    font-size: 30px;
    line-height: 34px;
    word-spacing: 8px;
  }

  .label--geneva .label-shape path { fill: var(--label-black); }
  .label--geneva .brand-mark { color: var(--ink-light); }
  .label--geneva .brand-name { color: var(--ink-light); }
  .label--geneva .line-sub { color: var(--ink-sage); }
  .label--geneva .wine-name { color: var(--wine-red); }
  .label--geneva .wine-origin { color: #a6aaa8; }

  .label--velmora .label-shape path { fill: var(--label-pearl); }
  .label--velmora .brand-mark,
  .label--velmora .brand-name,
  .label--velmora .wine-name { color: var(--ink-dark); }
  .label--velmora .line-sub,
  .label--velmora .wine-origin { color: var(--ink-sage); }

  .label--frontenac .label-shape path { fill: var(--label-rose); }
  .label--frontenac .brand-mark,
  .label--frontenac .brand-name,
  .label--frontenac .line-sub,
  .label--frontenac .wine-origin { color: var(--ink-plum); }
  .label--frontenac .wine-name { color: var(--wine-violet); }

  .label--crescent .label-shape path { fill: var(--label-cream); }
  .label--crescent .brand-mark,
  .label--crescent .brand-name { color: var(--ink-dark); }
  .label--crescent .line-sub,
  .label--crescent .wine-origin { color: var(--ink-sage); }
  .label--crescent .wine-name { color: var(--wine-amber); }
</style>
</head>
<body>

<section class="label label--geneva">
  <svg class="label-shape" viewBox="0 0 401 449" aria-hidden="true"><path d="M401 0 H172 Q118 6 112 73 Q40 100 28 216 Q2 226 0 254 V449 H401 Z"/></svg>
  <div class="label-text brand-mark">Harrow Ridge</div>
  <h2 class="label-text brand-name">Harrow Ridge<span class="line-sub">Cellars</span></h2>
  <p class="label-text wine-name">Geneva Red 7</p>
  <p class="label-text wine-origin">Iowa 2013</p>
</section>

<section class="label label--velmora">
  <svg class="label-shape" viewBox="0 0 401 449" aria-hidden="true"><path d="M401 0 H172 Q118 6 112 73 Q40 100 28 216 Q2 226 0 254 V449 H401 Z"/></svg>
  <div class="label-text brand-mark">Harrow Ridge</div>
  <h2 class="label-text brand-name">Harrow Ridge<span class="line-sub">Cellars</span></h2>
  <p class="label-text wine-name">Velmora Blush</p>
  <p class="label-text wine-origin">Iowa 2014</p>
</section>

<section class="label label--frontenac">
  <svg class="label-shape" viewBox="0 0 401 449" aria-hidden="true"><path d="M401 0 H172 Q118 6 112 73 Q40 100 28 216 Q2 226 0 254 V449 H401 Z"/></svg>
  <div class="label-text brand-mark">Harrow Ridge</div>
  <h2 class="label-text brand-name">Harrow Ridge<span class="line-sub">Cellars</span></h2>
  <p class="label-text wine-name">Frontenac Gris</p>
  <p class="label-text wine-origin">Iowa 2014</p>
</section>

<section class="label label--crescent">
  <svg class="label-shape" viewBox="0 0 401 449" aria-hidden="true"><path d="M401 0 H172 Q118 6 112 73 Q40 100 28 216 Q2 226 0 254 V449 H401 Z"/></svg>
  <div class="label-text brand-mark">Harrow Ridge</div>
  <h2 class="label-text brand-name">Harrow Ridge<span class="line-sub">Cellars</span></h2>
  <p class="label-text wine-name">La Crescent</p>
  <p class="label-text wine-origin">Iowa 2014</p>
</section>

</body>
</html>
```